Poster Design Project

We are a pizzeria based in Sydney CBD. Please see attached file for new website, do not use the current website look to make your graphic design.

We want to run a promotional campaign called " Rustico Rush".

Rustico Rush
$9 Pizza

Crispy & fresh dough topped with mouth watering mozzarella cheese, sprinkled with oregano and finished with fresh basil.

takeaway & eat in only
Medium Pizza Only (11 inch)

Target Market(s)

It is the lunch crowd in sydney cbd, predominately male but some female too. targeting the office workers.

Industry/Entity Type

Graphic Design

Requirements
Must have
• We are an Italian Pizzeria, so we would like an italian look and feel
our unique advantage is authentic and delicious thin crispy pizza
we want a nostalgic look and feel
some examples are attached of colours and style we like
Nice to have
• I can send you via email files to show you what the new website will look like

```html
<!DOCTYPE html>
<html lang="en">
<head>
<meta charset="utf-8">
<title>Rustico Rush – $9 Pizza</title>
<link rel="stylesheet" href="https://fonts.googleapis.com/css2?family=Oswald:wght@400;500&family=Rubik+Dirt&display=swap">
<style>
  :root {
    --black: #0b0b0b;
    --white: #ffffff;
    --green: #1f9a40;
    --red: #e6262c;
    --yellow: #f2e21a;
    --tomato: #c8321e;
  }
  * { margin: 0; padding: 0; box-sizing: border-box; }
  html, body { width: 960px; height: 1200px; overflow: hidden; background: var(--white); }
  .poster { position: relative; width: 960px; height: 1200px; overflow: hidden; background: var(--white); }

  .hero-photo {
    position: absolute; left: 0; top: 0; width: 960px; height: 308px;
    background:
      radial-gradient(ellipse 190px 150px at 480px 150px, #e9b566 0%, #d58a3e 55%, transparent 80%),
      radial-gradient(ellipse 200px 170px at 60px 120px, #e8a23c 0%, #b8561f 70%, transparent 90%),
      radial-gradient(ellipse 200px 170px at 900px 120px, #e8a23c 0%, #b8561f 70%, transparent 90%),
      linear-gradient(180deg, #7a2a16 0%, var(--tomato) 45%, #9b4a1c 100%);
  }

  .title-band {
    position: absolute; left: 0; top: 308px; width: 960px; height: 209px;
    background: var(--black); text-align: center;
    font-family: "Rubik Dirt", "Impact", sans-serif; text-transform: uppercase;
  }
  .title-band .campaign { position: absolute; left: 0; right: 0; top: 22px; font-size: 82px; letter-spacing: 5px; color: var(--white); line-height: 1; }
  .title-band .price { position: absolute; left: 0; right: 0; top: 110px; font-size: 74px; letter-spacing: 3px; color: var(--yellow); line-height: 1; }

  .flag-green, .flag-red { position: absolute; top: 517px; height: 530px; }
  .flag-green { left: 0; width: 325px; background: var(--green); }
  .flag-red { left: 630px; width: 330px; background: var(--red); }

  .description {
    position: absolute; left: 330px; width: 300px; top: 547px;
    font-family: "Oswald", "Arial Narrow", sans-serif; font-weight: 500;
    font-size: 33px; line-height: 59.5px; color: var(--black); text-align: center;
  }

  .footer-band { position: absolute; left: 0; top: 1047px; width: 960px; height: 153px; background: var(--black); }

  .brand-oval {
    position: absolute; left: 47px; top: 1033px; width: 266px; height: 160px;
    border-radius: 50%; background: var(--white);
    display: flex; align-items: center; justify-content: center;
  }
  .brand-oval .brand-name {
    font-family: "Oswald", "Arial Narrow", sans-serif; font-weight: 500;
    font-size: 34px; color: var(--red);
  }

  .terms { position: absolute; left: 453px; top: 1085px; text-transform: uppercase; }
  .terms .service { font-family: "Rubik Dirt", "Impact", sans-serif; font-size: 27px; color: var(--white); letter-spacing: 1px; line-height: 1; }
  .terms .size { margin-top: 12px; font-family: "Rubik Dirt", "Impact", sans-serif; font-size: 19px; color: var(--yellow); letter-spacing: 0.5px; line-height: 1; }
</style>
</head>
<body>
<main class="poster">
  <div class="hero-photo" role="img" aria-label="Photo of fresh pizzas topped with tomato slices, olives, peppers and basil"></div>

  <header class="title-band">
    <h1 class="campaign">Rustico Rush</h1>
    <p class="price">$9 Pizza</p>
  </header>

  <div class="flag-green" aria-hidden="true"></div>
  <div class="flag-red" aria-hidden="true"></div>

  <p class="description">
    Crispy &amp; Fresh Dough<br>
    Topped with<br>
    Mouth Watering<br>
    Mozzarella Cheese<br>
    Sprinkled with<br>
    Oregano And<br>
    Finished with<br>
    Fresh Basil.
  </p>

  <footer class="footer-band"></footer>
  <div class="brand-oval"><span class="brand-name">Casa Rustica</span></div>
  <div class="terms">
    <p class="service">Takeaway and Eat In Only</p>
    <p class="size">Medium Pizza Only (11 Inch)</p>
  </div>
</main>
</body>
</html>
```